Need new look for home page of Makeup Artist Site

We want a new, clean, modern, professional look for the new design for our website. Our current site is at https://glowvra.com. We would like a high fashion site with diverse ethnic groups represented throughout the page. We like trelk.com as an example of style and user experience. This website is for people to look for a makeup artist or esthetician to come to their home and perform a service there. They will pay on the website and be able to review available service providers and choose one. We will need 2 additional pages once this design is approved. We will pay separately for those.

```html
<!DOCTYPE html>
<html lang="en">
<head>
<meta charset="utf-8">
<title>Glowvra — Beauty and facial care at home</title>
<link rel="stylesheet" href="https://fonts.googleapis.com/css2?family=Montserrat:wght@300;400;500;600;700;800&family=Roboto+Condensed:ital,wght@1,700&family=Mrs+Saint+Delafield&family=Arimo:wght@400;700&display=swap">
<style>
:root{
  --red:#e3161b;
  --ink:#111111;
  --grey:#6b6b6b;
  --soft-grey:#a7a7a7;
  --blue:#1c3fd6;
  --footer:#161616;
  --footer-bar:#2f2f2f;
  --white:#ffffff;
  --nav-active:#f3e600;
}
*{box-sizing:border-box;margin:0;padding:0}
html,body{width:1200px;height:4209px;overflow:hidden;background:var(--white)}
body{position:relative;font-family:"Montserrat",sans-serif;color:var(--ink)}
.abs{position:absolute}

/* hero */
.hero{position:absolute;left:0;top:0;width:1200px;height:700px;
  background:radial-gradient(ellipse at 70% 55%,#f3b3a6 0%,#e98579 35%,#d94a48 70%,#c73034 100%)}
.hero-fade{position:absolute;left:0;top:700px;width:1200px;height:60px;background:linear-gradient(#f6d2d0,rgba(255,255,255,0))}
.account{top:36px;left:29px;font-size:17px;font-weight:700;color:var(--white)}
.account span{margin-right:20px}
.brand{top:22px;left:0;width:1200px;text-align:center;font-size:80px;font-weight:800;letter-spacing:2px;color:var(--ink);line-height:1}
.nav a{position:absolute;top:146px;font-size:21px;font-weight:600;color:var(--white);text-decoration:none;white-space:nowrap}
.nav a.active{color:var(--nav-active)}
.hero-title{top:262px;left:0;width:686px;text-align:center;font-size:55px;font-weight:400;color:var(--white);line-height:65px}
.learn{top:504px;left:222px;width:228px;height:44px;border:2px solid var(--white);color:var(--white);font-size:30px;font-weight:300;text-align:center;line-height:38px}
.slide-box{top:613px;left:0;width:101px;height:87px;background:rgba(120,40,40,.45)}
.slide-count{top:632px;left:120px;color:var(--white);font-size:18px;font-weight:300}
.slide-count b{font-size:34px;font-weight:700}

/* how it works */
.how-title{top:730px;left:0;width:1200px;text-align:center;font-family:"Roboto Condensed",sans-serif;font-style:italic;font-weight:700;font-size:68px;color:var(--ink)}
.red{color:var(--red)}
.col-title{font-size:48px;font-weight:500;border-bottom:2px solid var(--ink);line-height:56px}
.step-title{font-size:34px;font-weight:400;line-height:40px;white-space:nowrap}
.step-text{font-family:"Arimo",sans-serif;font-size:16.5px;line-height:21.5px;color:#555;width:290px}
.step-icon{width:30px;height:30px}
.pill{border:2px solid var(--blue);border-radius:6px;color:var(--blue);font-family:"Roboto Condensed",sans-serif;font-style:italic;font-weight:700;font-size:16px;text-align:center}

/* why */
.why-title{top:1540px;left:26px;font-family:"Roboto Condensed",sans-serif;font-style:italic;font-weight:700;font-size:62px}
.why-list{list-style:none;font-family:"Arimo",sans-serif;font-size:25px;color:var(--grey);line-height:31px}
.why-list li{position:absolute;left:96px;white-space:nowrap}
.why-list li::before{content:"";position:absolute;left:-38px;top:9px;width:16px;height:14px;border-radius:50%;background:var(--red)}
.photo{position:absolute}

/* services */
.discover{top:1930px;left:0;width:1200px;text-align:center;font-family:"Mrs Saint Delafield",cursive;font-size:130px;line-height:1}
.services-title{top:2050px;left:0;width:1200px;text-align:center;font-size:90px;font-weight:300;color:var(--red);line-height:1}
.service{position:absolute;width:300px;text-align:center}
.service .disc{width:216px;height:216px;border-radius:50%;margin:0 auto}
.service h3{font-size:26px;font-weight:700;letter-spacing:1.5px;line-height:31px;margin-top:22px}

/* contact */
.kicker{top:2955px;left:0;width:1200px;text-align:center;font-size:41px;font-weight:500;color:var(--soft-grey)}
.touch{top:3010px;left:0;width:1200px;text-align:center;font-size:68px;font-weight:800;letter-spacing:8px}
.field-label{font-family:"Arimo",sans-serif;font-size:25px;color:#333}
.field{border:1.5px solid #777;background:var(--white)}
.send{top:3756px;left:281px;width:203px;height:42px;background:var(--ink);color:var(--white);font-size:23px;font-weight:700;text-align:center;line-height:42px}

/* footer */
.footer{top:3963px;left:0;width:1200px;height:224px;background:var(--footer);color:var(--white)}
.footer h4{position:absolute;font-size:20px;font-weight:600;white-space:nowrap}
.footer ul{position:absolute;list-style:none;font-size:16.5px;line-height:29px;color:#ddd}
.footer .tiny{position:absolute;left:822px;top:75px;width:275px;font-size:7.5px;line-height:10px;color:#aaa;text-align:center}
.footer .email{position:absolute;left:822px;top:110px;width:274px;height:27px;border:1px solid #666;font-size:11px;color:#999;padding:6px 8px}
.footer .social{position:absolute;left:680px;width:16px;height:16px;border-radius:50%;background:var(--white)}
.bottom-bar{top:4187px;left:0;width:1200px;height:22px;background:var(--footer-bar);color:#ddd;font-size:13px;text-align:center;line-height:22px}
.bottom-bar i{display:inline-block;width:13px;height:13px;border:1.5px solid #ddd;border-radius:50%;vertical-align:-2px;margin-right:12px}
</style>
</head>
<body>

<header>
  <div class="hero" role="img" aria-label="Photo of a makeup artist applying eye makeup to a client, red toned"></div>
  <div class="hero-fade"></div>
  <div class="abs account"><span>Log in</span><span>Sign up</span></div>
  <div class="abs brand">GLOWVRA</div>
  <nav class="nav">
    <a class="active" style="left:59px">Home</a>
    <a style="left:168px">Services</a>
    <a style="left:307px">Consultants</a>
    <a style="left:486px">Apply to be a consultant</a>
    <a style="left:816px">Glowvra Street</a>
    <a style="left:1025px">Locations</a>
  </nav>
  <h1 class="abs hero-title">We provide beauty<br>and facial care services<br>at home.</h1>
  <div class="abs learn">Learn more...</div>
  <div class="abs slide-box"></div>
  <svg class="abs" style="left:40px;top:643px" width="18" height="28" viewBox="0 0 18 28"><path d="M15 2 3 14l12 12" fill="none" stroke="#fff" stroke-width="2"/></svg>
  <div class="abs slide-count">05 / <b>01</b></div>
  <svg class="abs" style="left:1140px;top:643px" width="18" height="28" viewBox="0 0 18 28"><path d="m3 2 12 12L3 26" fill="none" stroke="#fff" stroke-width="2"/></svg>
</header>

<section class="how">
  <h2 class="abs how-title">How <span class="red">Glowvra</span> Works</h2>

  <h3 class="abs col-title" style="left:128px;top:832px">For Clients</h3>
  <h3 class="abs col-title" style="left:651px;top:832px">For Consultants</h3>

  <svg class="abs step-icon" style="left:124px;top:925px" viewBox="0 0 30 30"><rect x="8" y="10" width="5" height="18" fill="#111"/><rect x="16" y="10" width="5" height="18" fill="#111"/><path d="M9 10 11 2l2 8z" fill="var(--red)"/></svg>
  <div class="abs step-title" style="left:159px;top:922px">Explore</div>
  <p class="abs step-text" style="left:162px;top:968px">Lorem Ipsum is simply dummy text of the printing and typesetting industry. Lorem Ipsum has been the industry's standard dummy</p>

  <svg class="abs step-icon" style="left:124px;top:1073px" viewBox="0 0 30 30"><rect x="4" y="4" width="20" height="25" rx="2" fill="none" stroke="#111" stroke-width="2.5"/><rect x="9" y="1" width="10" height="5" fill="#111"/><path d="M8 12h12M8 17h12M8 22h12" stroke="#111" stroke-width="2"/></svg>
  <div class="abs step-title" style="left:159px;top:1069px">Schedule</div>
  <p class="abs step-text" style="left:162px;top:1117px">Lorem Ipsum is simply dummy text of the printing and typesetting industry. Lorem Ipsum has been the industry's standard dummy</p>

  <svg class="abs step-icon" style="left:124px;top:1224px" viewBox="0 0 30 30"><rect x="6" y="2" width="12" height="22" rx="2" fill="none" stroke="#111" stroke-width="2.5"/><path d="M12 14c4 0 10 3 10 9v6H12z" fill="#111"/></svg>
  <div class="abs step-title" style="left:159px;top:1219px">Pay &amp; Get Glowvra</div>
  <p class="abs step-text" style="left:162px;top:1267px">Lorem Ipsum is simply dummy text of the printing and typesetting industry. Lorem Ipsum has been the industry's standard dummy</p>

  <svg class="abs step-icon" style="left:608px;top:920px;width:42px" viewBox="0 0 42 30"><circle cx="21" cy="9" r="6" fill="#111"/><circle cx="9" cy="11" r="4.5" fill="#111"/><circle cx="33" cy="11" r="4.5" fill="#111"/><path d="M11 27c0-8 4-11 10-11s10 3 10 11z M1 25c0-6 3-8 8-8s6 2 6 3l-2 5z M41 25c0-6-3-8-8-8s-6 2-6 3l2 5z" fill="#111"/></svg>
  <div class="abs step-title" style="left:659px;top:915px">Build your client base</div>
  <p class="abs step-text" style="left:661px;top:962px">Lorem Ipsum is simply dummy text of the printing and typesetting industry. Lorem Ipsum has been the industry's standard dummy</p>

  <svg class="abs step-icon" style="left:610px;top:1072px" viewBox="0 0 30 30"><circle cx="15" cy="15" r="12" fill="none" stroke="#111" stroke-width="3.5"/><path d="M15 8v8h-6" fill="none" stroke="#111" stroke-width="3"/></svg>
  <div class="abs step-title" style="left:659px;top:1066px">Manage your business</div>
  <p class="abs step-text" style="left:661px;top:1112px">Lorem Ipsum is simply dummy text of the printing and typesetting industry. Lorem Ipsum has been the industry's standard dummy</p>

  <svg class="abs step-icon" style="left:609px;top:1222px;width:40px" viewBox="0 0 40 30"><path d="M4 16 9 5h22l5 11v10h-5v-3H9v3H4z" fill="#111"/><path d="M11 8h18l3 8H8z" fill="#fff"/><circle cx="10" cy="19" r="2.5" fill="#fff"/><circle cx="30" cy="19" r="2.5" fill="#fff"/></svg>
  <div class="abs step-title" style="left:660px;top:1214px">Check appoinments and go</div>
  <p class="abs step-text" style="left:661px;top:1260px">Lorem Ipsum is simply dummy text of the printing and typesetting industry. Lorem Ipsum has been the industry's standard dummy</p>

  <div class="abs pill" style="left:191px;top:1400px;width:180px;height:31px;line-height:27px">Explore make-up looks</div>
  <div class="abs pill" style="left:693px;top:1396px;width:175px;height:33px;line-height:29px">Join Glowvra Network</div>
</section>

<section class="why">
  <h2 class="abs why-title">Why <span class="red">Glowvra</span> ?</h2>
  <ul class="why-list">
    <li style="top:1629px">Lorem Ipsum is simply dummy text of the prin</li>
    <li style="top:1677px">Lorem Ipsum is simply dummy inting and typesetting</li>
    <li style="top:1723px">Lorem Ipsum is simply dummy text of the printihupwcvg<br>Lorem I of the printing and typesetting</li>
    <li style="top:1804px">Lorem and typesetting</li>
    <li style="top:1853px">Limply dummy text of the printing and typesetting</li>
  </ul>
  <div class="photo" style="left:721px;top:1504px;width:280px;height:214px;background:linear-gradient(135deg,#eef2f7,#9cb4e0 45%,#d2455a 80%,#f2f2f2)" role="img" aria-label="Photo of makeup brushes, nail polish and cosmetics in a gift box"></div>
  <div class="photo" style="left:858px;top:1660px;width:313px;height:197px;background:linear-gradient(120deg,#3a1a1a 0%,#c9404a 30%,#f1c8b8 60%,#f7e2d8 100%);border:3px solid #fff;transform:rotate(1deg)" role="img" aria-label="Photo of a woman having blush applied with a brush"></div>
</section>

<section class="services">
  <div class="abs discover">Discover</div>
  <h2 class="abs services-title">our services</h2>

  <div class="service" style="left:-3px;top:2230px"><div class="disc" style="background:radial-gradient(circle,#f0c5a8,#e2735a 55%,#5d4a3c)" role="img" aria-label="Photo of hands holding a wedding bouquet"></div><h3>WEDDINGS</h3></div>
  <div class="service" style="left:296px;top:2230px"><div class="disc" style="background:radial-gradient(circle at 40% 40%,#7a6e6c,#1a1617 60%,#050505)" role="img" aria-label="Photo of a makeup brush with powder burst"></div><h3>FULL MAKE-UP<br>APPLICATION</h3></div>
  <div class="service" style="left:597px;top:2230px"><div class="disc" style="background:radial-gradient(circle,#c9776c,#9d5a55 55%,#d7dde1)" role="img" aria-label="Photo of a wrapped gift box"></div><h3>GIFT<br>CERTIFICATES</h3></div>
  <div class="service" style="left:896px;top:2230px"><div class="disc" style="background:radial-gradient(circle,#e15a4a,#b74037 50%,#8d7b6b)" role="img" aria-label="Photo of a large group at a party"></div><h3>GROUP PARTY</h3></div>

  <div class="service" style="left:-3px;top:2598px"><div class="disc" style="background:radial-gradient(circle at 60% 60%,#f6dcdb,#d99aa8 55%,#7d5a63)" role="img" aria-label="Photo of a woman holding a flower for facial care"></div><h3>FACIAL CARE</h3></div>
  <div class="service" style="left:290px;top:2598px"><div class="disc" style="background:radial-gradient(circle,#fbe8b6,#f6d98a 60%,#f2cf6e)" role="img" aria-label="Photo of hands applying cream from a tube"></div><h3>BEAUTY<br>TUITORIALS</h3></div>
  <div class="service" style="left:596px;top:2598px"><div class="disc" style="background:radial-gradient(circle,#7b6a60,#3f3532 55%,#1f1c1b)" role="img" aria-label="Photo of a man being groomed at a barber"></div><h3>MENS<br>GROOMING</h3></div>
  <div class="service" style="left:896px;top:2598px"><div class="disc" style="background:radial-gradient(circle at 60% 60%,#e8e8e8,#cfcfcf 60%,#5a5a5a)" role="img" aria-label="Photo of a pen signing a contract"></div><h3>CONTRACTS</h3></div>
</section>

<section class="contact">
  <div class="abs kicker">Contact Form</div>
  <h2 class="abs touch">GET IN TOUCH !</h2>

  <div class="abs field-label" style="left:280px;top:3145px">First name</div>
  <div class="abs field" style="left:281px;top:3178px;width:270px;height:31px"></div>
  <div class="abs field-label" style="left:644px;top:3145px">Last name</div>
  <div class="abs field" style="left:647px;top:3178px;width:270px;height:31px"></div>
  <div class="abs field-label" style="left:280px;top:3228px">Email</div>
  <div class="abs field" style="left:281px;top:3262px;width:636px;height:31px"></div>
  <div class="abs field-label" style="left:280px;top:3312px">Subject</div>
  <div class="abs field" style="left:281px;top:3347px;width:636px;height:31px"></div>
  <div class="abs field-label" style="left:280px;top:3397px">Message</div>
  <div class="abs field" style="left:281px;top:3438px;width:639px;height:298px"></div>
  <div class="abs send">Send message</div>
</section>

<footer>
  <div class="abs footer">
    <h4 style="left:92px;top:40px">About US</h4>
    <ul style="left:95px;top:67px"><li>Company</li><li>Services</li><li>User Agreement</li><li>Privacy Policy</li></ul>
    <h4 style="left:330px;top:38px">May we help you ?</h4>
    <ul style="left:347px;top:67px"><li>Contact Us</li><li>FAQ's</li><li>Service Care</li><li>Consultant portaL</li></ul>
    <h4 style="left:639px;top:40px">Find us on</h4>
    <span class="social" style="top:75px"></span>
    <span class="social" style="top:104px"></span>
    <h4 style="left:813px;top:38px">Sign up for GLOWVRA updates</h4>
    <p class="tiny">Enter your email address below to receive news about our latest services and early access to new offers.</p>
    <div class="email">Email id</div>
  </div>
  <div class="abs bottom-bar"><i></i>2019, GLOWVRA</div>
</footer>

</body>
</html>
```